Brochure Design Project

We are a consulting engineering company and need to have our current company brochure updated and made to look a lot more professional.

We provide design and documentation of electrical, lighting, mechanical, hydraulic, fire, services to architects, interior designers, building owners and managers.

We are launching an updated website shortly and want a print brochure to send to clients.

Attached is our current brochure for reference.
Updates

The recent projects section should be renamed to "Completed Projects". Space should be allowed for 8 projects. I have uploaded 7 of these images and a new image will follow shortly.

We would like to include an image for each of our company services. I have uploaded 9 new images:

1. Electrical
2. Mechanical
3. Communications
4. Fire
5. Security
6. Lighting
7. Hydraulics
8. Computer Suite
9. Building Assessments

Target Market(s)

Architects, Interior Designers, Consultants, Professionals

Industry/Entity Type

Building

Requirements
Must have
• Very professional look
Simple and easy to read layout
Similar look and feel to our new website which is soon to be launched : http://www.sitehaven.co.uk/rkm/
Examples of our recent projects - around 6 projects with 1 or 2 photos per project. Will upload these soon.
A3 size, double sided with centre fold
Should not have
• Bright colours
Any comics or similar

```html
<!DOCTYPE html>
<html lang="en">
<head>
<meta charset="utf-8">
<title>RKM Consulting Services – Brochure</title>
<link rel="stylesheet" href="https://fonts.googleapis.com/css2?family=Arimo:wght@400;700&family=Yanone+Kaffeesatz:wght@300&display=swap">
<style>
:root{
  --navy:#2f4655;
  --blue:#5574a6;
  --paper:#e9eaec;
  --white:#ffffff;
  --ink:#2b2f36;
  --heading:#2f4a6b;
  --soft:#c9d3dc;
}
*{margin:0;padding:0;box-sizing:border-box}
html,body{width:838px;height:1200px;overflow:hidden;background:var(--white)}
.canvas{position:relative;width:838px;height:1200px;overflow:hidden}
.sheet{position:absolute;left:0;top:0;width:1024px;height:1466px;transform:scale(.81836);transform-origin:0 0;font-family:"Arimo",Arial,sans-serif;color:var(--ink)}
.art{position:absolute;left:0;top:0}
.about{position:absolute;left:90px;top:46px;width:380px;font-size:9.8px;line-height:10px;letter-spacing:-.2px}
.about h2{font-size:10px;font-weight:700;color:var(--heading);margin:0 0 12px}
.about p{margin:0 0 10px;text-align:justify}
.about ul{list-style:none;margin:0 0 20px 16px}
.about li{padding-left:14px;position:relative}
.about li::before{content:"❖";position:absolute;left:0;font-size:8px}
.about .indent{margin-left:38px}
.about .tight{margin-bottom:10px}
.contact-bar{position:absolute;left:98px;top:657px;font-size:9.6px;color:var(--white)}
.contact-bar b{font-weight:700;margin-left:8px}
.contact-bar b:first-child{margin-left:0}
.quote{position:absolute;left:540px;top:426px;width:440px;text-align:center;font-family:"Yanone Kaffeesatz",sans-serif;font-weight:300;font-size:21px;line-height:24px;color:#c9d2da}
.brand{position:absolute;left:622px;top:600px;color:var(--navy)}
.brand .name{font-size:64px;font-weight:400;letter-spacing:-1px;line-height:60px}
.brand .tag{font-size:11.5px;font-weight:700;letter-spacing:3.3px;margin-top:4px;margin-left:20px}
.services{position:absolute;color:var(--white)}
.services h3{font-size:11.5px;font-weight:400;letter-spacing:.4px;margin-bottom:1px}
.services p{font-size:7.6px;line-height:9.3px;color:var(--soft)}
.services.left{left:44px}
.services.right{right:48px;text-align:right}
.office{position:absolute;left:44px;top:1264px;color:var(--white)}
.office .name{font-size:40px;line-height:44px;margin-bottom:22px}
.office p{font-size:11px;line-height:14px}
.office .gap{margin-top:12px}
</style>
</head>
<body>
<div class="canvas">
<div class="sheet">
<svg class="art" width="1024" height="1466" viewBox="0 0 1024 1466">
  <defs>
    <linearGradient id="paperPhoto" x1="0" y1="0" x2="1" y2="1">
      <stop offset="0" stop-color="#d9dadb"/><stop offset=".5" stop-color="#f2f2f1"/><stop offset="1" stop-color="#b9bcbf"/>
    </linearGradient>
    <linearGradient id="logoGround" x1="0" y1="0" x2="1" y2="0">
      <stop offset="0" stop-color="#f4f4f5"/><stop offset=".6" stop-color="#ffffff"/><stop offset="1" stop-color="#e2e3e5"/>
    </linearGradient>
    <linearGradient id="roomA" x1="0" y1="0" x2="0" y2="1">
      <stop offset="0" stop-color="#c9ccd0"/><stop offset=".5" stop-color="#8a7d72"/><stop offset="1" stop-color="#4f4c4b"/>
    </linearGradient>
    <linearGradient id="roomB" x1="0" y1="0" x2="0" y2="1">
      <stop offset="0" stop-color="#e6e6e4"/><stop offset=".6" stop-color="#cfcfcc"/><stop offset="1" stop-color="#6a6a6c"/>
    </linearGradient>
    <linearGradient id="roomC" x1="0" y1="0" x2="0" y2="1">
      <stop offset="0" stop-color="#3c3b3a"/><stop offset=".5" stop-color="#a9ac3e"/><stop offset="1" stop-color="#474641"/>
    </linearGradient>
    <linearGradient id="roomD" x1="0" y1="0" x2="0" y2="1">
      <stop offset="0" stop-color="#e8e9ea"/><stop offset=".6" stop-color="#d2d3d2"/><stop offset="1" stop-color="#545960"/>
    </linearGradient>
    <clipPath id="centreCut"><polygon points="298,750 748,750 688,1100 718,1450 332,1450 356,1100"/></clipPath>
  </defs>

  <rect x="16" y="15" width="496" height="601" fill="var(--paper)"/>
  <rect x="16" y="15" width="34" height="601" fill="var(--blue)"/>
  <rect x="16" y="616" width="496" height="100" fill="var(--navy)"/>
  <g role="img" aria-label="Photo of rolled architectural blueprints">
    <rect x="512" y="15" width="496" height="340" fill="url(#paperPhoto)"/>
  </g>
  <rect x="512" y="355" width="496" height="15" fill="var(--blue)"/>
  <rect x="512" y="370" width="496" height="167" fill="var(--navy)"/>
  <rect x="512" y="537" width="496" height="16" fill="var(--blue)"/>
  <rect x="512" y="553" width="496" height="163" fill="url(#logoGround)"/>

  <rect x="16" y="750" width="992" height="700" fill="var(--navy)"/>
  <polygon points="278,750 298,750 356,1100 332,1450 310,1450 336,1100" fill="var(--blue)"/>
  <polygon points="748,750 768,750 708,1100 740,1450 718,1450 688,1100" fill="var(--blue)"/>
  <g clip-path="url(#centreCut)">
    <rect x="280" y="750" width="480" height="700" fill="#e4e5e7"/>
    <g role="img" aria-label="Photo of a long boardroom table with brick wall and windows">
      <rect x="280" y="750" width="232" height="262" fill="url(#roomA)"/>
    </g>
    <g role="img" aria-label="Photo of a meeting room with projector screen">
      <rect x="512" y="750" width="250" height="262" fill="url(#roomB)"/>
    </g>
    <g role="img" aria-label="Photo of a green upholstered meeting booth">
      <rect x="280" y="1188" width="232" height="262" fill="url(#roomC)"/>
    </g>
    <g role="img" aria-label="Photo of an open plan office with desks">
      <rect x="512" y="1188" width="250" height="262" fill="url(#roomD)"/>
    </g>
  </g>
</svg>

<section class="about">
  <h2>ABOUT US</h2>
  <p>RKM was formed in November 1998 and has evolved into one of Perth's leading building services consulting practices.</p>
  <p>Our award winning projects cover all states and territories of Australia demonstrating our depth of experience.</p>
  <p>We work with all sectors of the property, infrastructure, mining, oil and gas and construction industries delivering, complex, multidiscipline building services engineering solutions.</p>
  <p>Our client base includes national, state and local governments, developers, tenants, builders, architects, project managers, interior designers and property/portfolio managers.</p>
  <p>RKM provides design, documentation and contract administration services associated with:</p>
  <ul>
    <li>Electrical</li><li>Mechanical</li><li>Communications</li><li>Fire</li><li>Security</li><li>Lighting</li><li>Hydraulics</li><li>Computer Suite</li><li>Building Assessments</li>
  </ul>
  <h2>OBJECTIVES</h2>
  <p>To provide the optimum, cost effective, energy efficient design solutions using the latest technological innovations.</p>
  <p>Our team at RKM aspires to:</p>
  <ul>
    <li>Surpass client expectation</li><li>Ensure client understanding of design concepts</li><li>Ensure timely provision of design input allowing ample time for consideration and inclusion</li>
  </ul>
  <h2>WORK ETHIC</h2>
  <ul class="tight">
    <li>To protect the engineering interests of our clients from initial involvement to the conclusion of each project</li>
  </ul>
  <p style="margin:-10px 0 0">To provide:</p>
  <ul class="indent">
    <li>A level of diligence, based on sound preparation that will ensure client satisfaction</li><li>Innovation in design</li><li>A service orientated and responsive approach</li><li>Continual implementation across all aspects of each project</li><li>A unique, detailed and focused approach to each project</li>
  </ul>
</section>

<div class="contact-bar"><b>T:</b> 08 9555 0142 <b>W:</b> www.rkmconsulting.com.au <b>E:</b> info@rkmconsulting.com.au</div>

<blockquote class="quote">“Every project receives a level of dedication, commitment and service to ensure client expectations are exceeded”</blockquote>

<div class="brand">
  <div class="name">rkm</div>
  <div class="tag">Consulting Services Pty Ltd</div>
</div>

<section class="services left" style="top:784px">
  <h3>Electrical Services</h3>
  <p>Power distribution<br>General lighting<br>Feature lighting for highlight/contrast of client orientated areas<br>Programmable lighting control<br>Emergency lighting and exit signs<br>Electrical consumption management<br>Lighting control integration with energy management systems<br>Evacuation warning systems<br>Power conditioners<br>Public address installations<br>Television signal distribution</p>
</section>
<section class="services left" style="top:924px">
  <h3>Critical Use Installations</h3>
  <p>Layout and space allowance for hardware and equipment<br>Uninterruptable power supplies and power conditioning<br>Access control and intruder detection<br>Fire rating<br>Anti static solutions<br>PABX and VOIP integration<br>Dedicated electrical distribution systems<br>Stand-by power supplies<br>High heat rejection cooling solutions</p>
</section>
<section class="services left" style="top:1046px">
  <h3>Computer Suite Audits</h3>
  <p>Comprehensive Computer Suite Audits<br>Australian Standard Compliance<br>TIA 942 Tier Rating certification</p>
</section>
<section class="services left" style="top:1111px">
  <h3>Hydraulic Services</h3>
  <p>Water supplies<br>Waste discharge<br>Venting<br>Water heating and cooling<br>Filtration</p>
</section>

<div class="office">
  <div class="name">rkm</div>
  <p>27 Carrow Street<br>Eastbrook, Western Australia&nbsp; 6091</p>
  <p class="gap">Phone : 08 9555 0142<br>Fax&nbsp;&nbsp;&nbsp;&nbsp;&nbsp; : 08 9555 0198</p>
  <p class="gap">Email&nbsp; : info@rkmconsulting.com.au</p>
</div>

<section class="services right" style="top:784px">
  <h3>Communication Systems</h3>
  <p>Telephone cabling<br>Data cabling<br>Patching philosophies<br>Fibre optic distribution systems<br>Integration of voice and<br>data cabling systems<br>Hardware housings<br>Compliance with relevant codes and installation practices<br>LAN Cable distribution systems</p>
</section>
<section class="services right" style="top:900px">
  <h3>Security Services</h3>
  <p>Electronic access control<br>Integration of existing systems with client requirements<br>Intruder detection<br>Off site monitoring and alarms<br>CCTV</p>
</section>
<section class="services right" style="top:980px">
  <h3>Fire Services</h3>
  <p>Electronic Smoke and Thermal Detection<br>Aspirating Smoke Systems<br>Fire Suppression Systems<br>Fire Sprinkler Systems</p>
</section>
<section class="services right" style="top:1055px">
  <h3>Mechanical Services</h3>
  <p>District Cooling System<br>Air and Water Cooled Chilled Water System<br>BMS/BAS and DDC Control System<br>Computer and Data Centre Solutions<br>DX-Type Water and Air<br>Cooled System (Single or<br>Multiple Indoor Units)<br>VAV and Chilled Beams<br>Industrial and Commercial<br>Humidification<br>Commercial and Industrial Evaporative Cooling Using Air<br>Washers</p>
</section>
<section class="services right" style="top:1199px">
  <h3>Building Assessment</h3>
  <p>Building services condition assessment<br>Advise relative to available building services (for long or short<br>term purpose)<br>Trouble Shooting and Investigation<br>Review of Existing Systems<br>Upgrade for Current and Future Refurbishment</p>
</section>
</div>
</div>
</body>
</html>
```